Criação de Kit Layout de Posts para Redes Sociais (Facebook, Instagram e etc) para Decoração & Mobília
" Empresa que desenvolve projetos e instalação de móveis planejados, utilizando o conceito moderno e inovador da marcenaria 4.0. "

```html
<!DOCTYPE html>
<html lang="pt-BR">
<head>
<meta charset="UTF-8">
<title>Post – VERTO Studio de Marcenaria</title>
<link rel="stylesheet" href="https://fonts.googleapis.com/css2?family=Montserrat:wght@300;400;500&display=swap">
<style>
  :root {
    --gold: #c8b07c;
    --gold-light: #e3d3ab;
    --navy: #0f1e3d;
    --white: #ffffff;
    --wall: #efedea;
    --wood: #9b6d48;
    --floor: #d8d0c4;
  }
  * { margin: 0; padding: 0; box-sizing: border-box; }
  html, body { width: 1200px; height: 1200px; overflow: hidden; background: var(--white); }
  .post {
    position: relative;
    width: 1200px;
    height: 1200px;
    overflow: hidden;
    font-family: "Montserrat", sans-serif;
  }
  .interior-photo {
    position: absolute;
    inset: 0;
    background:
      linear-gradient(90deg, rgba(255,255,255,0.35) 0%, rgba(255,255,255,0) 35%, rgba(255,255,255,0) 70%, rgba(255,255,255,0.15) 100%),
      linear-gradient(180deg,
        #f6f5f3 0%, var(--wall) 30%, #e9e5df 44%,
        #c9ad92 50%, #b08663 56%, var(--wood) 63%, #a87a55 70%,
        #c8b6a2 76%, var(--floor) 82%, #cfc5b8 100%);
  }
  .headline-banner { position: absolute; left: 0; top: 0; width: 1200px; height: 420px; }
  .headline {
    position: absolute;
    left: 140px;
    top: 118px;
    color: var(--white);
    font-weight: 300;
    line-height: 1;
    letter-spacing: 1px;
  }
  .headline .line-1 { display: block; font-size: 78px; }
  .headline .line-2 { display: block; font-size: 118px; margin-top: 8px; letter-spacing: 3px; }
  .footer-band { position: absolute; left: 0; bottom: 0; width: 1200px; height: 260px; }
  .brand {
    position: absolute;
    left: 84px;
    top: 1022px;
    display: flex;
    align-items: center;
    gap: 24px;
    color: var(--white);
  }
  .brand-mark {
    width: 66px;
    height: 140px;
    border: 3px solid var(--white);
  }
  .brand-name { font-weight: 300; }
  .brand-name .name { display: block; font-size: 88px; letter-spacing: 8px; line-height: 0.95; }
  .brand-name .tagline { display: block; font-size: 19px; letter-spacing: 3px; margin-top: 10px; }
  .contacts {
    position: absolute;
    left: 650px;
    top: 1078px;
    list-style: none;
    color: var(--white);
    font-size: 18px;
    font-weight: 400;
  }
  .contacts li { display: flex; align-items: center; gap: 8px; height: 40px; }
  .contacts .row { gap: 26px; }
  .contact-item { display: flex; align-items: center; gap: 8px; }
  .contact-icon { width: 26px; height: 26px; flex: none; }
</style>
</head>
<body>
<main class="post">
  <div class="interior-photo" role="img" aria-label="Quarto moderno com cama de linho claro, painel de madeira na parede, luminária de piso e poltrona de madeira com estofado bege"></div>

  <svg class="headline-banner" viewBox="0 0 1200 420" aria-hidden="true">
    <defs>
      <linearGradient id="goldFill" x1="0" y1="0" x2="1" y2="1">
        <stop offset="0" stop-color="#d4bf8e"/>
        <stop offset="1" stop-color="#b99c63"/>
      </linearGradient>
    </defs>
    <polygon points="0,120 955,120 925,390 0,390" fill="var(--gold-light)" opacity="0.55"/>
    <polygon points="0,84 920,84 880,356 0,356" fill="url(#goldFill)"/>
  </svg>
  <h1 class="headline"><span class="line-1">SEU TEXTO</span><span class="line-2">AQUI</span></h1>

  <svg class="footer-band" viewBox="0 0 1200 260" aria-hidden="true">
    <path d="M0,52 C320,18 760,8 1200,-10 L1200,260 L0,260 Z" fill="var(--gold)"/>
    <path d="M0,66 C320,34 760,26 1200,10 L1200,260 L0,260 Z" fill="var(--navy)"/>
  </svg>

  <div class="brand">
    <div class="brand-mark"></div>
    <div class="brand-name">
      <span class="name">VERTO</span>
      <span class="tagline">STUDIO DE MARCENARIA</span>
    </div>
  </div>

  <ul class="contacts">
    <li class="row">
      <span class="contact-item">
        <svg class="contact-icon" viewBox="0 0 28 28" aria-hidden="true">
          <circle cx="14" cy="14" r="14" fill="var(--gold)"/>
          <path d="M10 7.5c.8-.4 1.6 0 2 .8l1 2.2c.3.7.1 1.4-.5 1.8l-.9.6c.7 1.6 2 2.9 3.5 3.6l.6-.9c.4-.6 1.2-.8 1.8-.5l2.2 1c.8.4 1.2 1.2.8 2-.7 1.6-2.2 2.4-3.8 2-4.2-1-7.5-4.4-8.6-8.6-.3-1.6.4-3.1 1.9-4z" fill="var(--navy)"/>
        </svg>
        62 90000-000
      </span>
      <span class="contact-item">
        <svg class="contact-icon" viewBox="0 0 28 28" aria-hidden="true">
          <circle cx="14" cy="14" r="14" fill="var(--gold)"/>
          <circle cx="14" cy="14" r="3.2" fill="none" stroke="var(--navy)" stroke-width="1.8"/>
          <path d="M17.2 11v4.2c0 1.6 2.6 1.8 2.8-.4.4-4-2.4-6.6-6-6.6a5.8 5.8 0 1 0 3.4 10.5" fill="none" stroke="var(--navy)" stroke-width="1.8" stroke-linecap="round"/>
        </svg>
        @vertostudiomarcenaria
      </span>
    </li>
    <li>
      <svg class="contact-icon" viewBox="0 0 28 28" aria-hidden="true">
        <circle cx="14" cy="14" r="14" fill="var(--gold)"/>
        <g fill="none" stroke="var(--navy)" stroke-width="1.5">
          <circle cx="14" cy="14" r="7"/>
          <ellipse cx="14" cy="14" rx="3" ry="7"/>
          <line x1="7" y1="14" x2="21" y2="14"/>
        </g>
      </svg>
      www.vertostudiomarcenaria.com.br
    </li>
  </ul>
</main>
</body>
</html>
```